Pest Control - Brolga Pest Management

Pest Control
Termites (white ants)
Cockroaches
Ants
Spiders
Bed Bugs
Rats & Mice
Bird Proofing
Termite Inspections
Termite Baiting
Pest Identification

Commercial Services
Integrated Pest Management
Scheduled Servicing
Stored Product Pest
Rodent & Bird Control

Pre - Construction
Physical Termite Barriers
Chemical Barrier Installation
Reticulation Termite Barriers

Industry/Entity Type

Construction

Contact Information for Business Card

Callum: 0417 826 391
Tess: 0419 273 845

```html
<!DOCTYPE html>
<html lang="en">
<head>
<meta charset="utf-8">
<title>Brolga Pest Management – Business Card</title>
<link href="https://fonts.googleapis.com/css2?family=Arimo:wght@400;700&display=swap" rel="stylesheet">
<style>
  :root {
    --backdrop: #e4e4e4;
    --card-dark: #141414;
    --card-mid: #262626;
    --text-white: #f2f2f2;
    --text-grey: #9a9a9a;
    --accent-red: #e0202a;
    --watermark: rgba(255,255,255,0.07);
  }
  * { box-sizing: border-box; margin: 0; padding: 0; }
  html, body {
    width: 1200px; height: 800px; overflow: hidden;
    background: var(--backdrop);
    font-family: "Arimo", Arial, sans-serif;
  }
  .stage {
    position: relative; width: 1200px; height: 800px;
    display: flex; align-items: center; justify-content: center; gap: 40px;
  }
  .card {
    position: relative; width: 540px; height: 310px; overflow: hidden;
    background:
      repeating-linear-gradient(0deg, rgba(255,255,255,0.015) 0 1px, transparent 1px 3px),
      linear-gradient(160deg, var(--card-mid) 0%, var(--card-dark) 55%, #0d0d0d 100%);
    color: var(--text-white);
  }
  .watermark {
    position: absolute; font-weight: 700; color: var(--watermark);
    letter-spacing: -1px; white-space: nowrap;
  }
  /* Front */
  .front .watermark { right: 18px; bottom: 58px; font-size: 58px; }
  .brand-name {
    position: absolute; left: 36px; top: 112px;
    font-size: 30px; font-weight: 700; color: var(--text-white); line-height: 1.1;
    width: 240px;
  }
  .contacts {
    position: absolute; right: 30px; top: 26px; text-align: right;
  }
  .contact { margin-bottom: 10px; }
  .contact-name { font-size: 13px; color: var(--text-grey); }
  .contact-phone { font-size: 19px; color: var(--text-white); display: flex; align-items: center; justify-content: flex-end; gap: 8px; }
  .contact-phone svg { width: 10px; height: 14px; }
  .licence { font-size: 12px; color: var(--accent-red); }
  .email {
    position: absolute; right: 30px; top: 146px; font-size: 14px; color: var(--text-white);
    display: flex; align-items: center; gap: 8px;
  }
  .email svg { width: 14px; height: 10px; }
  .specialties {
    position: absolute; left: 36px; bottom: 26px; font-size: 12px; line-height: 1.35;
  }
  .specialties-title { color: var(--text-grey); }
  .specialties ul { list-style: none; }
  .specialties li { display: flex; align-items: center; gap: 6px; color: var(--text-white); }
  .specialties svg { width: 10px; height: 9px; flex: none; }
  /* Back */
  .back .watermark { right: 24px; bottom: 80px; font-size: 62px; }
  .kill-list {
    position: absolute; left: 0; right: 0; top: 78px; text-align: center;
    font-size: 13.5px; line-height: 1.45;
  }
  .kill-list h2 {
    font-weight: 400; font-size: 19px; color: var(--accent-red); margin-bottom: 4px;
  }
  .kill-list p { color: var(--text-white); }
  .mark { color: var(--accent-red); font-weight: 700; margin-right: 3px; }
</style>
</head>
<body>
<main class="stage">
  <section class="card front" aria-label="Business card front">
    <div class="watermark" aria-hidden="true">Brolga</div>
    <div class="brand-name">Brolga Pest Management</div>
    <div class="contacts">
      <div class="contact">
        <div class="contact-name">Callum</div>
        <div class="contact-phone">0417 826 391
          <svg viewBox="0 0 10 14"><rect x="1" y="1" width="8" height="12" rx="1.5" fill="none" stroke="#e0202a" stroke-width="1.5"/><rect x="3" y="3" width="4" height="5" fill="#e0202a"/></svg>
        </div>
        <div class="licence">LIC No: 1007342916</div>
      </div>
      <div class="contact">
        <div class="contact-name">Tess</div>
        <div class="contact-phone">0419 273 845
          <svg viewBox="0 0 10 14"><rect x="1" y="1" width="8" height="12" rx="1.5" fill="none" stroke="#e0202a" stroke-width="1.5"/><rect x="3" y="3" width="4" height="5" fill="#e0202a"/></svg>
        </div>
        <div class="licence">LIC No: 1005519832</div>
      </div>
    </div>
    <div class="email">office@brolgapest.com.au
      <svg viewBox="0 0 14 10"><rect x="0" y="0" width="14" height="10" rx="1" fill="#e0202a"/><path d="M1 1l6 5 6-5" fill="none" stroke="#141414" stroke-width="1.2"/></svg>
    </div>
    <div class="specialties">
      <div class="specialties-title">Specialise in</div>
      <ul>
        <li><svg viewBox="0 0 10 9"><path d="M1 5l3 3 5-7" fill="none" stroke="#e0202a" stroke-width="2"/></svg>Termite Eradication</li>
        <li><svg viewBox="0 0 10 9"><path d="M1 5l3 3 5-7" fill="none" stroke="#e0202a" stroke-width="2"/></svg>Termite Inspections</li>
        <li><svg viewBox="0 0 10 9"><path d="M1 5l3 3 5-7" fill="none" stroke="#e0202a" stroke-width="2"/></svg>General Pest Treatments</li>
        <li><svg viewBox="0 0 10 9"><path d="M1 5l3 3 5-7" fill="none" stroke="#e0202a" stroke-width="2"/></svg>Installation Chemical Barriers</li>
        <li><svg viewBox="0 0 10 9"><path d="M1 5l3 3 5-7" fill="none" stroke="#e0202a" stroke-width="2"/></svg>Installation Reticulation Barriers</li>
      </ul>
    </div>
  </section>

  <section class="card back" aria-label="Business card back">
    <div class="watermark" aria-hidden="true">Brolga</div>
    <div class="kill-list">
      <h2>Our Kill List</h2>
      <p><span class="mark">✕</span>Pest Control</p>
      <p><span class="mark">✕</span>Termites (white ants), <span class="mark">✕</span>Cockroaches</p>
      <p><span class="mark">✕</span>Ants, Spiders, <span class="mark">✕</span>Bed Bugs</p>
      <p><span class="mark">✕</span>Rats &amp; Mice, <span class="mark">✕</span>Bird Control</p>
      <p><span class="mark">✕</span>Termite Inspections, <span class="mark">✕</span>Termite Baiting <span class="mark">✕</span>Pest Identification</p>
      <p><span class="mark">✕</span>Integrated Pest Management, <span class="mark">✕</span>Scheduled Servicing</p>
      <p><span class="mark">✕</span>Stored Product Pest <span class="mark">✕</span>Rodent &amp; Bird Control</p>
    </div>
  </section>
</main>
</body>
</html>
```